Letterhead and envelope design

Using current logo and colours I would like to have a new design done for a stationary set to be printed.

The new files should include logo, web and email address as well as,mailing address and phone number

Dov Harmsby
Harmsby Construction Inc
Box 27 Site 18 RR5
Okotoks AB
T4K 2B9
Cell : 403-555-2917
Email: dov@harmsbyconstruction.example
web: harmsbyconstruction.example

```html
<!DOCTYPE html>
<html lang="en">
<head>
<meta charset="utf-8">
<title>Harmsby Construction Inc — Stationery Set</title>
<link href="https://fonts.googleapis.com/css2?family=Open+Sans:wght@400;600;700&display=swap" rel="stylesheet">
<style>
  :root{
    --navy:#1b3468;
    --orange:#c98a1e;
    --grey-band:#d3d5d8;
    --paper:#fbfbfb;
    --text-grey:#7a7d83;
    --stage:#cdcdcd;
  }
  *{box-sizing:border-box;margin:0;padding:0}
  html,body{width:1200px;height:968px;overflow:hidden}
  body{background:var(--stage);font-family:'Open Sans',Arial,sans-serif;position:relative}
  .sheet{position:absolute;background:var(--paper);box-shadow:0 6px 18px rgba(0,0,0,.18);overflow:hidden}
  .corner{position:absolute;display:block}
  .band-grey{fill:var(--grey-band)}
  .band-gap{fill:var(--paper)}
  .band-orange{fill:var(--orange)}
  .band-navy{fill:var(--navy)}

  .brand{display:flex;align-items:center;gap:12px}
  .brand-dot{border-radius:50%;background:var(--navy);flex:none}
  .brand-name{color:var(--navy);font-weight:600;line-height:1.1;text-transform:uppercase;letter-spacing:.02em}

  /* Letterhead */
  .letterhead{left:620px;top:60px;width:540px;height:700px}
  .letterhead .brand{position:absolute;left:40px;top:70px}
  .letterhead .brand-dot{width:62px;height:62px}
  .letterhead .brand-name{font-size:17px}
  .letterhead .contact{position:absolute;left:300px;top:66px;padding-left:14px;border-left:1px solid #d5d6d9;font-size:10.5px;line-height:1.6}
  .contact li{list-style:none;display:flex;align-items:flex-start;gap:7px;color:var(--text-grey);font-weight:600}
  .contact li.addr{color:var(--orange);font-weight:700}
  .contact svg{flex:none;margin-top:3px}

  /* Envelope */
  .envelope{left:40px;top:330px;width:540px;height:240px}
  .envelope .brand{position:absolute;left:26px;top:28px;align-items:flex-start}
  .envelope .brand-dot{width:60px;height:60px}
  .envelope .brand-name{font-size:15px;margin-top:6px}
  .envelope .return-addr{color:var(--orange);font-weight:700;font-size:11px;line-height:1.35;margin-top:4px}

  /* Business cards */
  .card-front{left:40px;top:80px;width:270px;height:155px;background:var(--navy)}
  .card-pattern{position:absolute;inset:0;background:linear-gradient(135deg,#223e78,#17305f)}
  .card-front .brand{position:absolute;left:34px;top:50px}
  .card-front .brand-dot{width:52px;height:52px;background:#fff}
  .card-front .brand-name{color:#fff;font-size:12px}

  .card-back{left:330px;top:80px;width:270px;height:155px}
  .card-back .strip{position:absolute;left:0;top:14px;width:100%;height:50px;background:#e4e5e7}
  .card-back .brand{position:absolute;right:22px;top:18px;gap:8px}
  .card-back .brand-dot{width:40px;height:40px}
  .card-back .brand-name{font-size:9.5px}
  .card-back .rule{position:absolute;left:20px;right:20px;top:76px;height:1px;background:var(--orange)}
  .card-back .person{position:absolute;left:20px;top:82px}
  .person-name{color:var(--orange);font-weight:600;font-size:12px}
  .person-role{color:var(--text-grey);font-size:7px}
  .card-back .contact{position:absolute;left:64px;top:100px;font-size:6.5px;line-height:1.5}
  .card-back .contact li{font-weight:400;color:var(--text-grey)}
  .card-back .contact li.addr{color:var(--orange);font-weight:600}
  .card-back .contact svg{margin-top:2px}
  .card-back .foot{position:absolute;left:0;bottom:0;width:100%;height:18px;background:linear-gradient(90deg,#2b57a6,var(--navy))}
  .card-back .foot-cut{position:absolute;right:0;bottom:0;width:62%;height:24px;background:var(--paper);border-top-left-radius:14px;border-top:2px solid #3c66b3}
</style>
</head>
<body>

<section class="sheet card-front">
  <div class="card-pattern" role="img" aria-label="Repeating brand monogram pattern on navy"></div>
  <div class="brand">
    <span class="brand-dot"></span>
    <span class="brand-name">Harmsby<br>Construction Inc</span>
  </div>
</section>

<section class="sheet card-back">
  <div class="strip"></div>
  <div class="brand">
    <span class="brand-dot"></span>
    <span class="brand-name">Harmsby<br>Construction Inc</span>
  </div>
  <div class="rule"></div>
  <div class="person">
    <p class="person-name">Dov Harmsby</p>
    <p class="person-role">Founder</p>
  </div>
  <ul class="contact">
    <li class="addr"><svg width="6" height="6"><circle cx="3" cy="3" r="3" fill="#1b3468"/></svg>Box 27 Site 18 RR5, Okotoks AB T4K 2B9</li>
    <li><svg width="6" height="6"><circle cx="3" cy="3" r="3" fill="#1b3468"/></svg>403-555-2917 &nbsp;·&nbsp; harmsbyconstruction.example</li>
    <li><svg width="6" height="6"><circle cx="3" cy="3" r="3" fill="#1b3468"/></svg>dov@harmsbyconstruction.example</li>
  </ul>
  <div class="foot"></div>
  <div class="foot-cut"></div>
</section>

<section class="sheet envelope">
  <svg class="corner" style="right:0;top:0" width="200" height="40" viewBox="0 0 200 40">
    <polygon class="band-grey" points="0,0 200,0 200,36"/>
    <polygon class="band-gap" points="0,0 200,0 200,31"/>
    <polygon class="band-orange" points="0,0 200,0 200,27"/>
    <polygon class="band-gap" points="0,0 200,0 200,23"/>
    <polygon class="band-navy" points="0,0 200,0 200,20"/>
  </svg>
  <div class="brand">
    <span class="brand-dot"></span>
    <div>
      <p class="brand-name">Harmsby<br>Construction Inc</p>
      <p class="return-addr">Box 27 Site 18 RR5, Okotoks<br>AB T4K 2B9</p>
    </div>
  </div>
  <svg class="corner" style="left:0;bottom:0" width="260" height="60" viewBox="0 0 260 60">
    <polygon class="band-grey" points="0,60 0,10 260,60"/>
    <polygon class="band-gap" points="0,60 0,16 260,60"/>
    <polygon class="band-orange" points="0,60 0,21 260,60"/>
    <polygon class="band-gap" points="0,60 0,27 260,60"/>
    <polygon class="band-navy" points="0,60 0,31 260,60"/>
  </svg>
</section>

<section class="sheet letterhead">
  <svg class="corner" style="right:0;top:0" width="260" height="52" viewBox="0 0 260 52">
    <polygon class="band-grey" points="0,0 260,0 260,50"/>
    <polygon class="band-gap" points="0,0 260,0 260,43"/>
    <polygon class="band-orange" points="0,0 260,0 260,38"/>
    <polygon class="band-gap" points="0,0 260,0 260,32"/>
    <polygon class="band-navy" points="0,0 260,0 260,28"/>
  </svg>
  <div class="brand">
    <span class="brand-dot"></span>
    <span class="brand-name">Harmsby<br>Construction Inc</span>
  </div>
  <ul class="contact">
    <li class="addr"><svg width="8" height="8"><circle cx="4" cy="4" r="3.2" fill="none" stroke="#c98a1e" stroke-width="1.4"/><circle cx="4" cy="4" r="1.2" fill="#c98a1e"/></svg>Box 27 Site 18 RR5<br>Okotoks AB T4K 2B9</li>
    <li><svg width="8" height="8" viewBox="0 0 8 8"><path d="M1 1h2l1 2-1 1a4 4 0 0 0 2 2l1-1 2 1v2C4 8 0 4 1 1z" fill="#7a7d83"/></svg>(403) 555-2917</li>
    <li><svg width="8" height="8"><rect x="0.5" y="1.5" width="7" height="5" fill="none" stroke="#c98a1e"/><path d="M.5 1.5l3.5 3 3.5-3" fill="none" stroke="#c98a1e"/></svg>dov@harmsbyconstruction.example</li>
    <li><svg width="8" height="8"><circle cx="4" cy="4" r="3.5" fill="#c98a1e"/></svg>www.harmsbyconstruction.example</li>
  </ul>
  <svg class="corner" style="left:0;bottom:0" width="320" height="80" viewBox="0 0 320 80">
    <polygon class="band-grey" points="0,80 0,12 320,80"/>
    <polygon class="band-gap" points="0,80 0,20 320,80"/>
    <polygon class="band-orange" points="0,80 0,27 320,80"/>
    <polygon class="band-gap" points="0,80 0,34 320,80"/>
    <polygon class="band-navy" points="0,80 0,39 320,80"/>
  </svg>
</section>

</body>
</html>
```